create making it look fantastic

create a name for this product and redesign this quick brochure i put together
GLINT ORBIT can not be used as it is already trademarked the word orbet

```html
<!DOCTYPE html>
<html lang="en">
<head>
<meta charset="utf-8">
<title>Volt Warden – Safety Above All</title>
<link rel="stylesheet" href="https://fonts.googleapis.com/css2?family=Bebas+Neue&family=Poppins:wght@400;500;600;700;800&display=swap">
<style>
  :root {
    --navy: #2a1454;
    --purple-deep: #1f0c45;
    --purple: #3a1a78;
    --orange: #f47b20;
    --orange-light: #f9a01b;
    --ink: #161616;
    --text: #2b2b2b;
    --white: #ffffff;
    --page: #efefef;
    --red: #d3141c;
    --yellow: #ffe21a;
  }
  * { box-sizing: border-box; margin: 0; padding: 0; }
  html, body { width: 783px; height: 1200px; overflow: hidden; background: var(--page); }
  body { font-family: "Poppins", sans-serif; color: var(--text); position: relative; }

  .flyer { position: absolute; left: 0; top: 93px; width: 783px; height: 1013px; display: flex; overflow: hidden; background: var(--white); }

  /* Left column */
  .info { width: 423px; position: relative; padding: 0 35px 0 50px; }
  .brand { position: absolute; top: 62px; left: 0; width: 423px; display: flex; justify-content: center; align-items: center; gap: 10px; }
  .brand-dot { width: 16px; height: 16px; border-radius: 50%; background: var(--orange); }
  .brand-name { font-family: "Poppins", sans-serif; font-weight: 800; font-size: 34px; letter-spacing: 1px; color: var(--navy); line-height: 1; }

  .headline { position: absolute; top: 156px; left: 0; width: 423px; text-align: center; }
  .headline-lead { font-size: 35px; font-weight: 400; color: var(--ink); line-height: 1.1; }
  .headline-key { font-family: "Bebas Neue", sans-serif; font-size: 158px; color: var(--orange); line-height: 0.82; letter-spacing: 2px; margin-top: 2px; }
  .headline-tail { font-size: 59px; font-weight: 800; color: var(--ink); line-height: 1; margin-top: -2px; letter-spacing: -0.5px; }
  .divider { position: absolute; top: 379px; left: 52px; width: 337px; height: 2px; background: #d4d4d4; }

  .section-title { font-size: 23px; font-weight: 700; color: var(--orange); line-height: 1; padding-left: 12px; border-left: 3px solid var(--navy); }
  .application { position: absolute; top: 403px; left: 50px; width: 340px; }
  .application p { font-size: 12.6px; line-height: 1.22; color: var(--text); margin-top: 0; }
  .application p + p { margin-top: 14px; }
  .application .section-title { margin-bottom: 14px; }
  .application strong { font-weight: 600; color: var(--ink); }

  .features { position: absolute; top: 617px; left: 50px; width: 340px; }
  .features .section-title { margin-bottom: 14px; }
  .feature-list { list-style: none; }
  .feature-list li { position: relative; padding-left: 19px; font-size: 12.4px; font-weight: 600; color: var(--ink); line-height: 1.05; margin-bottom: 13px; }
  .feature-list li::before { content: ""; position: absolute; left: 3px; top: 3px; width: 7px; height: 7px; border-radius: 50%; border: 2px solid var(--navy); }
  .accent { color: var(--orange); }

  .contact { position: absolute; top: 886px; left: 53px; width: 360px; }
  .contact-call { font-size: 20px; font-weight: 400; color: var(--ink); line-height: 1; }
  .contact-call strong { font-weight: 700; color: var(--navy); }
  .contact-lines { display: flex; align-items: center; gap: 8px; margin-top: 18px; font-size: 14.5px; font-weight: 500; color: var(--ink); }
  .contact-lines span { display: inline-flex; align-items: center; gap: 5px; }

  /* Right column */
  .showcase { width: 360px; position: relative; background: linear-gradient(180deg, var(--purple-deep) 0%, var(--purple) 38%, #4a2070 55%, var(--orange) 66%, var(--orange) 85%, var(--orange-light) 100%); color: var(--white); }
  .specs { position: absolute; top: 52px; left: 43px; width: 300px; }
  .specs-title { font-size: 23px; font-weight: 700; color: var(--orange); line-height: 1; margin-bottom: 12px; }
  .spec-list { list-style: none; }
  .spec-list li { position: relative; padding-left: 17px; font-size: 12.6px; font-weight: 500; line-height: 1.1; margin-bottom: 14px; }
  .spec-list li::before { content: ""; position: absolute; left: 1px; top: 4px; width: 7px; height: 7px; border-radius: 50%; border: 2px solid var(--orange); }

  .product-photo { position: absolute; left: 0; top: 362px; width: 370px; height: 370px; border-radius: 50%; background: radial-gradient(circle at 45% 45%, #6a6f78 0%, #3d4149 45%, #e9e9e9 62%, #ffffff 70%); border: 10px solid var(--white); }
  .ribbon { position: absolute; left: 78px; top: 678px; width: 200px; height: 36px; }
  .badge { position: absolute; left: 170px; top: 300px; width: 120px; height: 120px; border-radius: 50%; background: var(--red); border: 4px solid #f3c7c9; display: flex; flex-direction: column; align-items: center; justify-content: center; text-align: center; }
  .badge-title { font-size: 30px; font-weight: 800; color: var(--yellow); line-height: 1; }
  .badge-sub { font-size: 10.5px; font-weight: 600; line-height: 1.05; text-transform: uppercase; }

  .danger { position: absolute; left: 22px; top: 802px; width: 292px; height: 102px; border: 1.5px solid var(--purple-deep); border-radius: 6px; text-align: center; }
  .danger-head { position: absolute; left: 0; right: 0; top: -22px; display: flex; justify-content: center; align-items: center; gap: 4px; }
  .danger-head-inner { display: inline-flex; align-items: center; gap: 6px; background: var(--orange); padding: 0 6px; }
  .danger-word { font-size: 34px; font-weight: 800; color: var(--white); line-height: 1; letter-spacing: 0.5px; }
  .danger-risk { margin-top: 26px; font-size: 19px; font-weight: 700; color: var(--purple-deep); line-height: 1.1; }
  .danger-note { font-size: 13px; color: var(--white); margin-top: 4px; }

  .website { position: absolute; left: 0; width: 360px; top: 929px; text-align: center; font-size: 17.5px; font-weight: 600; color: var(--white); }
</style>
</head>
<body>
<main class="flyer">
  <section class="info">
    <div class="brand">
      <span class="brand-dot"></span>
      <span class="brand-name">VOLT WARDEN</span>
    </div>

    <header class="headline">
      <p class="headline-lead">Prioritizing Your</p>
      <h1 class="headline-key">SAFETY</h1>
      <p class="headline-tail">ABOVE ALL</p>
    </header>
    <div class="divider"></div>

    <section class="application">
      <h2 class="section-title">APPLICATION</h2>
      <p>Our GPO is easily installed by a <strong>registered electrician and once it is turned on and customised,</strong> it will only operate for up to 8 hours.</p>
      <p>Prevent the risk to your environment of <strong>battery operated wheelchairs and scooters.</strong></p>
      <p>The 8-Hour warden keeps a battery operating equipment safe from <strong>overheating and possibly exploding.</strong></p>
    </section>

    <section class="features">
      <h2 class="section-title">FEATURES</h2>
      <ul class="feature-list">
        <li><span class="accent">FIRE</span> retardent double GPO made with V0 material.</li>
        <li>Tempered glass panel easily cleaned and never fades.</li>
        <li>Capacitive easy touch power on button.</li>
        <li>MCU Intelligent Smart Chipset, 3 Year Warranty.</li>
        <li>Automatic cut-off of power 2 hours (can be customised).</li>
        <li>Complies with Australian Standards and Approvals.</li>
      </ul>
    </section>

    <footer class="contact">
      <p class="contact-call">CONTACT FOR <strong>FREE ESTIMATE</strong></p>
      <div class="contact-lines">
        <span>
          <svg width="15" height="15" viewBox="0 0 24 24" aria-hidden="true"><path fill="#2a1454" d="M6.6 10.8a15.1 15.1 0 0 0 6.6 6.6l2.2-2.2c.3-.3.7-.4 1-.2 1.1.4 2.3.6 3.6.6.6 0 1 .4 1 1V20c0 .6-.4 1-1 1A17 17 0 0 1 3 4c0-.6.4-1 1-1h3.5c.6 0 1 .4 1 1 0 1.3.2 2.5.6 3.6.1.3 0 .7-.2 1z"/></svg>
          012.555.0147
        </span>
        <span>
          <svg width="15" height="11" viewBox="0 0 24 16" aria-hidden="true"><rect x="1" y="1" width="22" height="14" fill="#2a1454"/><path d="M1 1l11 8 11-8" fill="none" stroke="#fff" stroke-width="1.6"/></svg>
          info@voltwarden.example
        </span>
      </div>
    </footer>
  </section>

  <section class="showcase">
    <div class="specs">
      <h2 class="specs-title">SPECIFICATIONS</h2>
      <ul class="spec-list">
        <li>Colours available with and black.</li>
        <li>Size 120 x 72 x 42mm.</li>
        <li>Capacitive easy touch power on button.</li>
        <li>Operating Voltage: 110-240V AC/50Hz-60Hz.</li>
        <li>Rated Current: 10A x 2</li>
        <li>Material: toughened glass panel + fire retardant shel</li>
      </ul>
    </div>

    <div class="product-photo" role="img" aria-label="Photo of the dark glass double power outlet inside a white ring with a Safety First ribbon"></div>

    <div class="badge">
      <span class="badge-title">NEW</span>
      <span class="badge-sub">Innovative<br>Technology</span>
    </div>

    <div class="danger">
      <div class="danger-head">
        <span class="danger-head-inner">
          <svg width="40" height="34" viewBox="0 0 40 34" aria-hidden="true"><path d="M20 2 L38 32 H2 Z" fill="#d3141c" stroke="#d3141c" stroke-width="3" stroke-linejoin="round"/><rect x="18" y="11" width="4" height="12" rx="2" fill="#fff"/><circle cx="20" cy="27" r="2.3" fill="#fff"/></svg>
          <span class="danger-word">DANGER</span>
        </span>
      </div>
      <p class="danger-risk">RISK OF BATTERY<br>EXPLOSION</p>
      <p class="danger-note">No smoking sparks or flames</p>
    </div>

    <p class="website">www.voltwarden.example</p>
  </section>
</main>
</body>
</html>
```